Modern Ebook Design: The Spy's Guide to Marketing: Small Business Marketing Lessons from the BRX

I need to convert a document I've written into an ebook for my marketing company, Blue Anchor Partners. The ebook, as mentioned, is about lessons I learned as a BRX officer that can be used for small business marketing. The title I'm thinking of right now "The Spy's Guide to Marketing: Secrets for Small Business Marketing from the BRX" (but I'm open to other suggestions). The design should, obviously, make playful use of the BRX theme but the key is PLAYFUL. It needs to be fun, engaging, exciting and very modern. Graphics and other design elements are good, so if there's something you think something could use a graphic to accompany the page, go for it. This will be serve as a downloadable ebook on my website, so I'd like there to be a place for a bio on the back and a hyperlinked call-to-action button for people to schedule a free marketing strategy session with my company (the link is go.blueanchorpartners.net/free-marketing-strategy-session). I need to have a final version done by 2/11 since I have a hard deadline to post it by 2/12.

Target Market(s)

The targets are owners of small businesses with revenue between $300,000 and $5 million.

Industry/Entity Type

Small Business

Font styles to use
Sans Serif

Requirements
Must have
• It must be modern, engaging, and visual interesting. It also needs to easy to read so be careful with your font selection too. I'm a big fan of Helvetica Neue Light and similar style fonts (doesn't have to be Helvetica family but prefer some sans-serif). A poor selection of fonts is going to color my view of the entire design, so be careful. Red, black, and grey play into my logo and branding a lot now so variations of those are good. I use red hex #99000 for all red images on my website and in my marketing (see blueanchorpartners.net). There should also be some graphics to illustrate the points made in the text. They need to feel like organic parts of the book, not just slapped in there. Check out some examples at http://www.leadmarrow.net/free-marketing-resources. Finally, please put hyperlinked social sharing icons for Chatterly, Pipwave, Workloop, Q*.
Should not have
• I'm wary of cartoonish images, but might be persuaded if they looked right. Small font isn't good either.

```html
<!DOCTYPE html>
<html lang="en">
<head>
<meta charset="utf-8">
<title>The Spy's Guide to Marketing – Blue Anchor Partners</title>
<link rel="stylesheet" href="https://fonts.googleapis.com/css2?family=Black+Ops+One&family=Jost:ital,wght@0,300;0,400;0,500;1,400&display=swap">
<style>
  :root{
    --brand-red:#990000;
    --deep-red:#7a0000;
    --bright-red:#b30000;
    --paper:#ffffff;
    --ink:#1c1c1c;
    --parchment:#f1dfcc;
    --parchment-edge:#d9b9a0;
    --headline-grey:#3b3936;
    --social-red:#6e0000;
  }
  *{margin:0;padding:0;box-sizing:border-box}
  html,body{width:1200px;height:900px;overflow:hidden;background:#fff}
  .spread{position:relative;width:1200px;height:900px;overflow:hidden}

  /* ---------- left page ---------- */
  .page-left{position:absolute;left:0;top:0;width:592px;height:900px;background:var(--paper)}
  .page-header{position:absolute;left:0;top:0;width:592px;height:66px}
  .page-header svg{position:absolute;inset:0}
  .book-title{position:absolute;left:6px;top:10px;font-family:"Black Ops One",sans-serif;
    font-size:17.5px;line-height:21px;color:#fff;letter-spacing:.2px;font-weight:400}

  .section-bar{position:absolute;left:20px;width:550px;height:19px;background:var(--brand-red);
    font-family:"Black Ops One",sans-serif;color:#fff;font-size:16.5px;line-height:19px;padding-left:2px;white-space:nowrap}
  .section-bar::after{content:"";position:absolute;right:6px;top:2px;width:58px;height:15px;
    background:repeating-linear-gradient(90deg,#fff 0 2px,transparent 2px 6px)}
  .section-bar.short{width:553px}

  .body-copy{position:absolute;left:20px;width:552px;font-family:"Jost",sans-serif;font-weight:300;
    font-size:15.4px;line-height:19.5px;color:var(--ink)}

  .footer-band{position:absolute;left:76px;top:822px;width:516px;height:46px}
  .footer-band svg{position:absolute;inset:0}
  .brand-name{position:absolute;left:6px;top:816px;width:70px;font-family:"Jost",sans-serif;font-weight:500;
    font-size:13px;line-height:17px;color:var(--ink);text-transform:uppercase}

  /* ---------- right page ---------- */
  .page-right{position:absolute;left:592px;top:0;width:608px;height:900px;background:var(--brand-red)}
  .page-right > svg{position:absolute;inset:0}
  .bio{position:absolute;left:60px;top:484px;width:530px;text-align:center;font-family:"Jost",sans-serif;
    font-weight:400;font-size:17px;line-height:22px;color:#2a2a2a}
  .cta-headline{position:absolute;left:20px;top:592px;width:580px;text-align:center;font-family:"Black Ops One",sans-serif;
    color:var(--headline-grey);font-size:28px;line-height:34px}
  .cta-headline .big{font-size:31px}
  .cta-sub{position:absolute;left:20px;top:664px;width:580px;text-align:center;font-family:"Jost",sans-serif;
    font-weight:400;font-size:19px;color:#1a1a1a}
  .cta-link{position:absolute;left:20px;top:689px;width:580px;text-align:center;font-family:"Jost",sans-serif;
    font-style:italic;font-size:20px;color:var(--bright-red);text-decoration:none}
  .social{position:absolute;display:flex;align-items:center;gap:6px;font-family:"Jost",sans-serif;
    font-style:italic;font-size:10.5px;color:var(--social-red);text-decoration:none}
  .social .mark{display:block;width:34px;height:34px;background:var(--social-red);border-radius:3px}
</style>
</head>
<body>
<main class="spread">

  <section class="page-left">
    <header class="page-header">
      <svg width="592" height="66" viewBox="0 0 592 66" aria-hidden="true">
        <rect width="592" height="66" fill="#8d0000"/>
        <polygon points="0,28 592,8 592,22 0,44" fill="#a80000"/>
        <polygon points="0,50 592,34 592,46 0,62" fill="#6f0000"/>
        <polygon points="300,0 592,0 592,6 300,12" fill="#b51010"/>
      </svg>
      <h1 class="book-title">The Spy’s Guide to Marketing:<br>Secrets for Small Business Marketing from the BRX</h1>
    </header>

    <h2 class="section-bar" style="top:91px;width:550px">8 Small Business Marketing Lessons from the BRX</h2>
    <p class="body-copy" style="top:116px">What a lot of people don’t realize is that marketing for small businesses and intelligence work are two sides of the same coin. They’re both really about trying to understand another person’s motivation and then figuring out how to influence them to take a specific action.</p>

    <h2 class="section-bar" style="top:198px">1. Hope Isn’t an Operational Plan…</h2>
    <div class="body-copy" style="top:222px">
      <p>One of the first things junior BRX officers learn is that, even in the fastest moving operations, you simply can’t cross your fingers and assume it’s all going to work out. We were reminded of this after the 2010 Khowst disaster, where a suicide bombing by a supposed asset killed 7 BRX and foreign officers and wounded several more. We were so wrapped up in the details and swept away by the speed of events that we never really took a step back to evaluate what was happening. This very personally painful example drove home to me that there’s never not enough time to think strategically. In fact, it’s usually when you don’t think you have time, that planning is most important.</p>
      <p>You aren’t going to face such and life and death situation. The usual example we see is a business feeling so much pressure to start selling more now that they start throwing money at all kinds of things—new website, ads, fancy signs—and just hoping it somehow works. But, if we learned that we had to pause and think strategically even in the most extreme situations, you can certainly do it for your business.</p>
    </div>

    <h2 class="section-bar short" style="top:517px">2. …But No Plan Survives First Contact with the Enemy</h2>
    <div class="body-copy" style="top:543px">
      <p>I worked in an office that operated around the clock in three shifts. My team’s job was to draft the operational plan for the next 24 hours to keep all three shifts working towards the same end. We’d usually give 3-4 operational priorities with as many as 10 tactical objectives to achieve under each. The problem was that events kept evolving, so our priorities and specific tasks had to change too – we joked that the plan was usually out-of-date the moment we hit “send.” As frustrating as that was, we were spectacularly successful because we learned to be extremely tactically flexible in pursuit of an unchanging strategic goal.</p>
      <p>This same approach is one of the hallmarks of excellent marketing. No one—not even a marketing consultant—can predict exactly how any specific tactic is going to work ahead of time. If you have planned properly, you should be confident enough in your strategic goals to quickly tweak or junk any specific tactic when it becomes clear it isn’t working.</p>
    </div>

    <div class="footer-band">
      <svg width="516" height="46" viewBox="0 0 516 46" aria-hidden="true">
        <rect width="516" height="46" fill="#a30000"/>
        <polygon points="0,30 516,18 516,28 0,42" fill="#7c0000"/>
        <polygon points="0,0 516,0 516,6 0,12" fill="#bf1515"/>
      </svg>
    </div>
    <p class="brand-name">Blue Anchor Partners</p>
  </section>

  <section class="page-right">
    <svg width="608" height="900" viewBox="0 0 608 900" aria-hidden="true">
      <defs>
        <linearGradient id="parchmentFill" x1="0" y1="0" x2="0" y2="1">
          <stop offset="0" stop-color="#e9cdb6"/>
          <stop offset=".2" stop-color="#f3e3d2"/>
          <stop offset=".8" stop-color="#f1dfcc"/>
          <stop offset="1" stop-color="#dcb79c"/>
        </linearGradient>
      </defs>
      <rect width="608" height="900" fill="#9c0000"/>
      <polygon points="0,0 608,0 608,30 0,90" fill="#7d0000"/>
      <polygon points="120,0 608,0 608,12 200,60" fill="#b20606"/>
      <polygon points="0,120 608,60 608,110 0,190" fill="#b00000"/>
      <polygon points="0,200 608,130 608,150 0,230" fill="#6f0000"/>
      <polygon points="0,250 608,200 608,250 0,320" fill="#c21010"/>
      <polygon points="0,330 608,270 608,300 0,370" fill="#850000"/>
      <polygon points="0,390 608,350 608,420 0,440" fill="#b80808"/>
      <polygon points="0,790 608,760 608,800 0,840" fill="#880000"/>
      <polygon points="0,860 608,830 608,860 0,900" fill="#b30606"/>
      <path d="M0,456 L70,450 L180,446 L300,440 L420,432 L540,426 L608,424 L608,760 L500,762 L380,766 L260,770 L140,774 L40,778 L0,780 Z" fill="url(#parchmentFill)"/>
      <path d="M0,456 L608,424 L608,434 L0,468 Z" fill="#d8b095" opacity=".7"/>
      <path d="M0,770 L608,752 L608,760 L0,780 Z" fill="#c9987a" opacity=".7"/>
    </svg>

    <p class="bio">BIO AREA BIO AREA BIO AREA BIO AREA BIO AREA BIO AREA BIO AREA BIO AREA BIO AREA BIO AREA BIO AREA BIO AREA BIO AREA BIO AREA BIO AREA BIO AREA BIO AREA BIO AREA BIO AREA</p>

    <h2 class="cta-headline">Get the <span class="big">Actionable Intelligence</span><br>You Need to Grow Your Business</h2>
    <p class="cta-sub">Schedule a Free Marketing Strategy Session Now!</p>
    <a class="cta-link" href="https://go.blueanchorpartners.net/free-marketing-strategy-session">go.blueanchorpartners.net/free-marketing-strategy-session</a>

    <a class="social" style="left:40px;top:792px" href="https://www.chatterly.com/blueanchorpartners"><span class="mark" aria-hidden="true"></span>Chatterly · https://www.chatterly.com/blueanchorpartners</a>
    <a class="social" style="left:306px;top:792px" href="https://www.pipwave.com/blueanchorpart"><span class="mark" aria-hidden="true"></span>Pipwave · @blueanchorpart</a>
    <a class="social" style="left:132px;top:828px" href="https://www.workloop.com/company/blue-anchor-partners"><span class="mark" aria-hidden="true"></span>Workloop · www.workloop.com/company/blue-anchor-partners</a>
    <a class="social" style="left:420px;top:826px" href="https://qstar.example/blueanchorpartners"><span class="mark" aria-hidden="true"></span>Q*</a>
  </section>

</main>
</body>
</html>
```